Meridel Capra SA Business Cards

Dear all,
Thank you for reading my brief and project. My company is doing doing advisory in real estate and to comapnies + real estates services as asset management, brokerage, development etc.
I would like to get a business card for my company which is clear, professionnal and serious.
Please have a look to the attachement to see the logos of the company

Industry/Entity Type

Real Estate

Contact Information for Business Card

I would like to have in the business card the following
Principal side:
- Logo of the company (or Monogram)
- First and Last Name (Paulo Vestrand)
- Mobile number
- email address

Second side:
- Address (Chemin des Orvets 17, 1226 Thônex - Switzerland)
- website (www.meridelcapra.ch)

Requirements
Must have
• Refer to the typeface and logo colors

```html
<!DOCTYPE html>
<html lang="en">
<head>
<meta charset="utf-8">
<title>Meridel Capra SA – Business Cards</title>
<link href="https://fonts.googleapis.com/css2?family=Montserrat:wght@600&family=Work+Sans:wght@400;600&display=swap" rel="stylesheet">
<style>
  :root {
    --stage: #1c1c1c;
    --card: #272727;
    --card-edge: #2e2e2e;
    --blue: #1a7fd0;
    --white: #f4f4f4;
    --grey: #e2e2e2;
  }
  * { margin: 0; padding: 0; box-sizing: border-box; }
  html, body { width: 1200px; height: 900px; overflow: hidden; background: var(--stage); }
  .canvas {
    width: 1200px; height: 900px;
    display: flex; flex-direction: column; align-items: center; justify-content: center; gap: 40px;
  }
  .card {
    position: relative;
    width: 700px; height: 400px;
    background: linear-gradient(135deg, var(--card) 0%, var(--card-edge) 100%);
    border-bottom: 5px solid var(--blue);
    display: flex; align-items: center;
  }
  .brand { display: flex; align-items: center; gap: 22px; }
  .brand-mark { width: 46px; height: 46px; background: var(--blue); }
  .brand-rule { width: 2px; height: 90px; background: var(--blue); }
  .brand-name {
    font-family: "Montserrat", sans-serif; font-weight: 600;
    font-size: 26px; letter-spacing: 1px; color: var(--white); white-space: nowrap;
  }
  .card-front { justify-content: center; }
  .card-back { padding-left: 70px; }
  .card-back .brand-name { font-size: 22px; }
  .card-back .brand-rule { height: 80px; }
  .divider { width: 2px; height: 230px; background: var(--blue); margin: 0 36px 0 54px; }
  .contact { font-family: "Work Sans", sans-serif; color: var(--grey); font-size: 17px; line-height: 1.35; }
  .person-name { color: var(--blue); font-size: 27px; font-weight: 400; line-height: 1.1; }
  .person-name .first { font-weight: 600; }
  .person-role { font-size: 17px; margin-bottom: 14px; }
  .address { margin-bottom: 12px; }
  .contact-line { display: flex; align-items: center; gap: 10px; }
  .contact-line svg { width: 13px; height: 13px; flex: none; }
</style>
</head>
<body>
<main class="canvas">
  <section class="card card-front">
    <div class="brand">
      <div class="brand-mark"></div>
      <div class="brand-rule"></div>
      <div class="brand-name">MERIDEL CAPRA</div>
    </div>
  </section>

  <section class="card card-back">
    <div class="brand">
      <div class="brand-mark"></div>
      <div class="brand-rule"></div>
      <div class="brand-name">MERIDEL CAPRA</div>
    </div>
    <div class="divider"></div>
    <div class="contact">
      <div class="person-name"><span class="first">Paulo</span> Vestrand</div>
      <div class="person-role">Principal</div>
      <div class="address">Chemin des Orvets 17,<br>1226 Thônex<br>Switzerland</div>
      <div class="contact-line">
        <svg viewBox="0 0 16 16"><path d="M4 1 L6.5 1 L7.5 4.5 L5.8 6 C6.6 8 8 9.4 10 10.2 L11.5 8.5 L15 9.5 L15 12 C15 13.5 13.8 15 12 15 C6 14.5 1.5 10 1 4 C1 2.2 2.5 1 4 1 Z" fill="var(--blue)"/></svg>
        <span>1234 567 8900</span>
      </div>
      <div class="contact-line">
        <svg viewBox="0 0 16 16"><rect x="1" y="3" width="14" height="10" fill="none" stroke="var(--blue)" stroke-width="1.6"/><path d="M1 3 L8 9 L15 3" fill="none" stroke="var(--blue)" stroke-width="1.6"/></svg>
        <span>info@meridelcapra.ch</span>
      </div>
      <div class="contact-line">
        <svg viewBox="0 0 16 16"><g fill="none" stroke="var(--blue)" stroke-width="1.3"><circle cx="8" cy="8" r="6.5"/><ellipse cx="8" cy="8" rx="3" ry="6.5"/><path d="M1.5 8 H14.5 M2.5 4.8 H13.5 M2.5 11.2 H13.5"/></g></svg>
        <span>www.meridelcapra.ch</span>
      </div>
    </div>
  </section>
</main>
</body>
</html>
```